Graphic Design/Logo Needed for Ear Drops Bottle

We have an Ear Drop Medication that we need to create a new label for. We will use a retro picture of a Doctor (Dr. Blenham) and the name of the product is Tidy Lobe. There is no official logo, so we will want to create a retro, basic logo for Tidy Lobe and use the retro picture. Front portion of the label is Size is 1.5" in height, and about 1.375" Width. this is a small tube similar in size to eye drops. We will be looking for just the logo portion and what you will see on the front of the bottle.

Target Market(s)

Medical Container

Industry/Entity Type

Medical

Font styles to use
Serif
Sans Serif

Colors
0054AA
0677BA
7BADD7
CADEEF
E8F1F8
FFF300
FFF600
FEFA6F
FFFEC7
FFFEE8

Requirements
Must have
• Picture of Dr. Blenham, "Tidy Lobe", Dr. Blenham's Ear Solution
Nice to have
• Retro Style or Modern with Retro Feel, Clean and engaging

```html
<!DOCTYPE html>
<html lang="en">
<head>
<meta charset="utf-8">
<title>Tidy Lobe — Earache Drops Label</title>
<link rel="stylesheet" href="https://fonts.googleapis.com/css2?family=Libre+Caslon+Text:wght@400;700&display=swap">
<style>
  :root {
    --ink: #0d0b0a;
    --paper: #ffffff;
    --cream: #f8f1e9;
    --beige: #e4cdb4;
    --tan: #c9a27d;
    --gold: #a58a5e;
    --sepia-light: #e9dcc6;
    --sepia-dark: #8a7558;
  }
  * { box-sizing: border-box; margin: 0; padding: 0; }
  html, body { width: 967px; height: 1200px; overflow: hidden; background: var(--paper); }
  body { font-family: "Libre Caslon Text", Georgia, serif; color: var(--ink); position: relative; }

  /* Primary logo */
  .brand-mark {
    position: absolute; left: 307px; top: 70px; width: 352px; height: 352px;
    border-radius: 50%; background: var(--cream);
    border: 9px solid var(--ink);
    box-shadow: inset 0 0 0 6px var(--cream), inset 0 0 0 8px var(--ink);
    display: flex; flex-direction: column; align-items: center; justify-content: center; text-align: center;
  }
  .brand-mark .brand-name { font-size: 66px; font-weight: 700; line-height: 1; letter-spacing: 1px; }
  .brand-mark .brand-tagline { margin-top: 18px; font-size: 21px; font-weight: 700; letter-spacing: .5px; }

  /* Labels */
  .label {
    position: absolute; top: 520px; width: 400px; height: 417px; overflow: hidden;
  }
  .label--dark { left: 60px; background: var(--ink); color: var(--sepia-light); }
  .label--beige { left: 507px; background: var(--beige); color: var(--ink); }

  .label .title-box {
    position: absolute; left: 27px; top: 17px; width: 238px; height: 86px;
    border: 1.5px solid var(--gold); padding: 18px 0 0 28px;
    font-size: 22px; line-height: 1.15; letter-spacing: 1px;
  }
  .label--beige .title-box { background: var(--ink); color: var(--beige); }
  .label .side-rule {
    position: absolute; left: 27px; top: 103px; width: 1.5px; height: 230px; background: var(--gold);
  }
  .label .base-rule {
    position: absolute; left: 27px; top: 333px; width: 238px; height: 1.5px; background: var(--gold);
  }

  .label .portrait {
    position: absolute; right: 0; top: 0; width: 150px; height: 370px;
    background: linear-gradient(180deg, var(--sepia-light) 0%, #cdb998 45%, var(--sepia-dark) 100%);
  }
  .label--dark .portrait {
    -webkit-mask-image: linear-gradient(90deg, transparent 0%, #000 35%);
            mask-image: linear-gradient(90deg, transparent 0%, #000 35%);
  }

  .label .badge {
    position: absolute; left: 41px; top: 121px; width: 216px; height: 216px; border-radius: 50%;
    background: var(--cream); border: 6px solid var(--ink);
    box-shadow: 0 0 0 5px var(--paper);
    display: flex; flex-direction: column; align-items: center; justify-content: center;
    color: var(--ink); text-align: center;
  }
  .label .badge .brand-name { font-size: 40px; font-weight: 700; line-height: 1; }
  .label .badge .brand-tagline { margin-top: 10px; font-size: 12.5px; font-weight: 700; }

  .label .info-strip {
    position: absolute; left: 0; bottom: 0; width: 100%; height: 60px; color: var(--ink);
  }
  .label--dark .info-strip { background: linear-gradient(180deg, #d9d4d8 0%, var(--paper) 40%); }
  .label .ages { position: absolute; left: 37px; top: 8px; font-size: 19px; }
  .label .volume { position: absolute; left: 30px; top: 33px; font-size: 12px; }
  .label .claim { position: absolute; left: 209px; top: 8px; font-size: 18px; line-height: 1.15; }
</style>
</head>
<body>

  <div class="brand-mark">
    <div class="brand-name">Tidy Lobe</div>
    <div class="brand-tagline">DR. BLENHAM'S EAR SOLUTION</div>
  </div>

  <section class="label label--dark">
    <div class="portrait" role="img" aria-label="Retro sepia photograph of Dr. Blenham wearing a head mirror and white coat"></div>
    <div class="title-box">EARACHE<br>DROPS</div>
    <div class="side-rule"></div>
    <div class="base-rule"></div>
    <div class="badge">
      <div class="brand-name">Tidy Lobe</div>
      <div class="brand-tagline">DR. BLENHAM'S EAR SOLUTION</div>
    </div>
    <div class="info-strip">
      <div class="ages">AGES 2+</div>
      <div class="volume">0,33 FL. OZ. (10ML)</div>
      <div class="claim">RELIEVE EAR<br>PAIN FAST</div>
    </div>
  </section>

  <section class="label label--beige">
    <div class="portrait" role="img" aria-label="Retro sepia photograph of Dr. Blenham wearing a head mirror and white coat"></div>
    <div class="title-box">EARACHE<br>DROPS</div>
    <div class="side-rule"></div>
    <div class="base-rule"></div>
    <div class="badge">
      <div class="brand-name">Tidy Lobe</div>
      <div class="brand-tagline">DR. BLENHAM'S EAR SOLUTION</div>
    </div>
    <div class="info-strip">
      <div class="ages">AGES 2+</div>
      <div class="volume">0,33 FL. OZ. (10ML)</div>
      <div class="claim">RELIEVE EAR<br>PAIN FAST</div>
    </div>
  </section>

</body>
</html>
```